Web design for cloud computing startup

Our company is called BrightLedgerHub and we are a cloud computing startup that automates the purchasing to payment process for any company. This is a B2B solution targeting small and medium enterprises across different industries. Our application allows buyers to create electronic purchase orders and send them to suppliers. In turn, suppliers can generate invoices based on purchase orders. In addition to organizing and formalizing interactions between buyers and suppliers our system is environment friendly as it significantly reduces the amount of paper buyers and suppliers use.

Our mission is to become the leader on the market of cloud based software for procurement by delivering easy-integrated and cost effective solutions to help our customers improve operational efficiency and boost profitability of business.

We need your help to design 2 pages:
- Homepage
- Content page

Please use 3 colors for the webpages: white, blue, and green. White and blue should be primary colors, while green should just emphasize that we are environment friendly solution.

The words we are using to describe the website are the following:
- Simple and minimalist
- Modern, clean and light
- Professional and reliable
- Creative (we want something different from standard website template)
- Calling to action

Please see attached design examples for homepage and content page that we like (please note that attached examples are only for the page structures not for the color schemes).

In addition to features mentioned in the attached ppt, homepage should have:
- Rotating banner with 3 different pictures (one of them featuring environmental aspect of our solution)
- Contact us on Pagewall, Quello, Tramvoy

Reason: I've updated the project brief, eliminating some of the requirements giving you more freedom.

Reason: Requests from designers to extend deadline

Target Market(s)

Small and Medium Enterprises. Primary users of the website are senior executives of those companies so website needs to account for this.

Industry/Entity Type

Environment

Requirements
Must have
• - For the final design we need PSD files with all the original layers
- The width needs to be a size that will work with every size computer screen
- Need to use cross-platform compatible font

Please feel free to ask any questions to help you refine your design.
Look forward to seeing your designs. Thank you all for your time and efforts.

```html
<!DOCTYPE html>
<html lang="en">
<head>
<meta charset="utf-8">
<title>BrightLedgerHub — Managed Cloud Computing</title>
<link href="https://fonts.googleapis.com/css2?family=Arimo:wght@400;700&display=swap" rel="stylesheet">
<style>
:root{
  --page:#ffffff;
  --page-soft:#f3f8fc;
  --panel:#f7fafd;
  --panel-edge:#cfdfed;
  --text:#3e4a56;
  --text-dim:#7a8794;
  --white:#ffffff;
  --blue:#1f7fc9;
  --blue-deep:#135a96;
  --blue-light:#d9eaf7;
  --green:#5aa83a;
  --green-deep:#3f8327;
  --sky:#9cc6ea;
}
*{box-sizing:border-box;margin:0;padding:0}
html,body{width:889px;height:1200px;overflow:hidden}
body{
  position:relative;
  font-family:"Arimo",Arial,sans-serif;
  color:var(--text);
  background:linear-gradient(180deg,var(--blue-light) 0,var(--page-soft) 120px,var(--page) 420px,var(--page) 100%);
  font-size:10px;
}
.abs{position:absolute}
/* header */
.brand{left:24px;top:34px;display:flex;align-items:center;gap:8px}
.brand-mark{width:14px;height:14px;border-radius:50%;background:var(--green)}
.brand-name{font-size:21px;color:var(--blue-deep);font-weight:400;line-height:1}
.follow{right:30px;top:12px;display:flex;align-items:center;gap:5px;font-size:8px;color:var(--text-dim)}
.social{width:12px;height:12px;border-radius:2px;background:var(--blue)}
.social.two{background:var(--sky)}.social.three{background:var(--blue-deep)}
.support{left:360px;top:56px;font-size:9px;color:var(--text)}
.support b{color:var(--green-deep)}
.search{left:700px;top:52px;display:flex}
.search input{width:110px;height:16px;border:1px solid var(--panel-edge);background:var(--white);font-size:8px;padding:0 4px;font-family:inherit}
.search button{width:36px;height:16px;border:0;background:var(--blue);color:var(--white);font-size:8px;font-family:inherit}
.nav{left:350px;top:97px;width:510px;height:18px;background:var(--blue);display:flex;align-items:center;border-radius:3px 3px 0 0}
.nav a{color:var(--white);text-decoration:none;font-size:9px;padding:0 9px;line-height:18px}
.nav a.active{background:var(--blue-deep)}
.nav a.eco{background:var(--green)}
/* banner */
.banner{left:24px;top:122px;width:836px;height:262px;border-radius:6px;overflow:hidden;
  background:linear-gradient(135deg,#f4f9fd 0,#dcebf7 45%,#b8d4ea 100%)}
.banner-photo{left:0;top:0;width:330px;height:262px;background:linear-gradient(160deg,#eef4f9,#b6cce0)}
.banner-title{left:300px;top:14px;font-size:20px;color:var(--white);background:var(--blue);padding:3px 10px;border-radius:3px}
.banner-list{left:360px;top:58px;list-style:none;font-size:11px;color:var(--blue-deep);font-weight:700;line-height:19px}
.banner-list li::before{content:"\25B8  ";color:var(--green)}
.dots{left:400px;top:240px;display:flex;gap:6px}
.dots span{width:8px;height:8px;border-radius:50%;background:#a9c3d9}
.dots span:first-child{background:var(--green)}
/* sections */
h2{font-weight:400;color:var(--blue);font-size:17px}
.haze-title{left:36px;top:424px}
.haze-img{left:36px;top:466px;width:230px;height:102px;background:linear-gradient(180deg,#9cc4ea,#3f6fa8)}
.haze-text{left:282px;top:470px;width:570px;font-size:9px;line-height:12px}
.haze-text p+p{margin-top:10px}
.why-title{left:36px;top:580px}
.why-img{left:36px;top:620px;width:52px;height:38px;background:linear-gradient(180deg,#d6e6f4,#6f96c4)}
.why-text{left:98px;top:622px;width:754px;font-size:9px;line-height:12px}
/* panels */
.panel{top:710px;height:238px;background:linear-gradient(180deg,var(--white),var(--panel));border:1px solid var(--panel-edge);border-radius:5px}
.panel h3{position:absolute;left:12px;top:10px;font-size:11px;font-weight:400;color:var(--blue-deep)}
.panel-video{left:30px;width:326px}
.panel-why{left:362px;width:260px}
.panel-login{left:628px;width:232px}
.video-frame{left:12px;top:30px;width:302px;height:158px;background:linear-gradient(180deg,#eef5fc,#a9cbea)}
.video-caption{left:12px;top:196px;width:302px;font-size:8px;line-height:11px;color:var(--text-dim)}
.why-frame{left:12px;top:30px;width:236px;height:112px;background:linear-gradient(180deg,#f1f5f9,#c3d3e3)}
.why-caption{left:12px;top:150px;width:236px;font-size:8px;line-height:11px;color:var(--text-dim)}
.more{font-size:8px;color:var(--green-deep)}
.panel-video .more{left:260px;top:220px}
.panel-why .more{left:196px;top:220px}
.login{left:12px;top:34px;width:206px;font-size:8px;color:var(--text-dim)}
.login label{display:block;margin-top:8px}
.login input{display:block;width:140px;height:16px;border:1px solid var(--panel-edge);background:var(--white);margin-top:3px}
.login button{margin-top:12px;width:44px;height:16px;border:0;background:var(--green);color:var(--white);font-size:8px;font-family:inherit}
.login .forgot{margin-left:8px}
/* footer */
.footer-band{left:0;top:958px;width:889px;height:150px;
  background:linear-gradient(180deg,var(--blue-deep) 0,var(--blue) 35%,var(--blue-deep) 100%)}
.footer-cols{left:30px;top:972px;display:flex;gap:14px}
.footer-col{width:98px;font-size:8px;line-height:11px;color:#d4e7f6;list-style:none}
.footer-col li:first-child{color:var(--white);font-weight:700;margin-bottom:3px}
.footer-base{left:0;top:1108px;width:889px;height:92px;background:var(--page-soft);border-top:3px solid var(--green)}
.footer-brand{left:30px;top:1124px;font-size:15px;color:var(--blue-deep)}
.copy{left:30px;top:1146px;font-size:7px;color:var(--text-dim)}
.footer-follow{right:40px;top:1130px;display:flex;align-items:center;gap:5px;font-size:8px;color:var(--text-dim)}
</style>
</head>
<body>
<header>
  <div class="abs brand"><span class="brand-mark"></span><span class="brand-name">BrightLedgerHub</span></div>
  <div class="abs follow">Follow us on social network <span class="social one" aria-label="Pagewall"></span><span class="social two" aria-label="Quello"></span><span class="social three" aria-label="Tramvoy"></span></div>
  <div class="abs support">Click here to our Support: <b>Toll Free 1-800-555-0142</b></div>
  <form class="abs search"><input type="text" placeholder="Search"><button type="button">Search</button></form>
  <nav class="abs nav"><a class="active">Home</a><a>Company</a><a>Solution</a><a>How to work</a><a class="eco">Save the Earth</a><a>Knowledge center</a><a>Contact us</a></nav>
</header>

<section class="abs banner">
  <div class="abs banner-photo" role="img" aria-label="Businessman holding up a cloud against a pale sky"></div>
  <div class="abs banner-title">Welcome to our Managed Cloud Computing Services</div>
  <ul class="abs banner-list">
    <li>No Experience or Extra Staff Needed</li>
    <li>Websites Runs Smoothly 24/7</li>
    <li>Stay Up-to-Date</li>
    <li>Hosting Services Grow with Your Business</li>
    <li>Good Return on Investment</li>
  </ul>
  <div class="abs dots"><span></span><span></span><span></span></div>
</section>

<main>
  <h2 class="abs haze-title">Break Through the Haze around Cloud Computing</h2>
  <div class="abs haze-img" role="img" aria-label="Person standing on a hill under a blue sky with clouds"></div>
  <div class="abs haze-text">
    <p>We invite you to download a new white paper on one of today's most important technology trends: cloud computing. This emerging area of technology promises to deliver new levels of IT efficiency and agility, elastic scalability, and enhanced value quality of service.</p>
    <p>This white paper explains Nimbrel's cloud computing strategy and how Nimbrel helps customers and partners adopt cloud computing, plan their evolution toward a cloud model, and realise the full benefits of cloud computing.</p>
  </div>
  <h2 class="abs why-title">Why Choose Us</h2>
  <div class="abs why-img" role="img" aria-label="Small cloud themed picture"></div>
  <p class="abs why-text">Our network delivers purchase orders, invoices and payments in one simple place, so teams spend less time on paper and more time on growth. Setup is quick, support is always on, and every record stays safe in the cloud. Buyers and suppliers work together clearly, costs drop, and less paper means a lighter footprint for every business we serve.</p>

  <section class="abs panel panel-video">
    <h3>BLH Video</h3>
    <div class="abs video-frame" role="img" aria-label="Video still titled What is Cloud Computing with cloud drawings"></div>
    <p class="abs video-caption">Our short video walks you through cloud computing and how orders and invoices move between buyers and suppliers.</p>
    <span class="abs more">Read more ›</span>
  </section>

  <section class="abs panel panel-why">
    <h3>Why BLH</h3>
    <div class="abs why-frame" role="img" aria-label="Team of office workers in a bright meeting room"></div>
    <p class="abs why-caption">Trusted by growing firms to cut paper, speed up approvals and keep every supplier on the same page.</p>
    <span class="abs more">Read more ›</span>
  </section>

  <section class="abs panel panel-login">
    <h3>Client Login</h3>
    <form class="abs login">
      <label>Username<input type="text"></label>
      <label>Password<input type="password"></label>
      <button type="button">Login</button><span class="forgot">Forgot password?</span>
    </form>
  </section>
</main>

<footer>
  <div class="abs footer-band"></div>
  <div class="abs footer-cols">
    <ul class="footer-col"><li>Home</li><li>About BLH</li><li>Why BLH</li><li>Customer testimonials</li><li>Our management</li><li>Careers</li></ul>
    <ul class="footer-col"><li>Company</li><li>Purchase to pay process</li><li>For suppliers</li><li>For buyers</li><li>Pricing</li><li>Implementation</li><li>Privacy policy</li></ul>
    <ul class="footer-col"><li>Solution</li><li>Order flow</li><li>Invoice flow</li><li>Payments</li></ul>
    <ul class="footer-col"><li>How to work</li><li>Speed up your business</li><li>Simplify your operations</li><li>Manage documents</li></ul>
    <ul class="footer-col"><li>Save the Earth</li><li>Industry news</li><li>White papers</li><li>Training materials</li><li>Success stories</li><li>FAQ</li></ul>
    <ul class="footer-col"><li>Knowledge center</li><li>Help desk</li><li>Guides</li></ul>
    <ul class="footer-col"><li>Contact us</li><li>Sales</li><li>Support</li></ul>
  </div>
  <div class="abs footer-base"></div>
  <div class="abs footer-brand">BrightLedgerHub</div>
  <div class="abs copy">© BrightLedgerHub. All Rights Reserved.</div>
  <div class="abs footer-follow">Follow us on social network <span class="social one"></span><span class="social two"></span><span class="social three"></span></div>
</footer>
</body>
</html>
```